Nutritional & Gastrointestinal Health Consulting Service-Website design

We need a website design for a new health consulting service called "Bright Meadow" based in Perth, Australia.

We will be providing consulting services in the areas of:
1) Nutrition and Diet
2) Gastrointestinal Health (which means stomach & digestive system related health)

These consulting services will be provided by an Accredited Dietitian and a Paediatric Gastroenterologist.

We are open to creative ideas in terms of design, layout, fonts and colours. We also would love to see images of nature in the backdrop with families (adults with kids) having a good time, fresh fruits and vegetables displayed in a farmer's market or supermarket. 2 or 3 images should be sufficient. We would also definitely want our logo somewhere in the main page of website. The logo file is also attached. Please have a look at a website's design that we really liked. We would love to see designs inspired by that style. The website details are in the in the "nice to have priorities" section of this project brief.

We also would be looking at website designers with software coding skills so that if we like the design we can go ahead with the next step of coding.

The website design should communicate the purpose of the website and at the same time be simple, elegant and unique/eye-catching.

We look forward to receiving creative ideas for our website from you all. Good luck!

More details have been added to our project- for example: Logo, fonts style, must haves etc etc. Please view the updated project brief. Looking forward to receiving your fantastic ideas for our website. Thanking you

Hi, I have updated the colour preference. Will add the content preferences tomorrow. thanks

Hello all, I have now added a LOT more content to what we want in our website. It is very much in detail, so please carefully have a read through the entire project brief. If you have any questions write back to me and I will try to respond as quickly as I can. Last few days were busy so couldn't respond quickly to all of you who had send me designs/queries/questions. Thank you for your patience. I look forward to receiving fantastic designs from you all. Good Luck :-)

Target Market(s)

Adults based in western speaking countries aged 18 to 60 years

Industry/Entity Type

Software

Font styles to use
Sans Serif
Script

Colors
faa54b
acd036

Requirements
Must have
• The website must have the MAIN logo file attached. I have attached 3 files: 1) MAIN logo; 2) supplementary logo A ; 3) supplementary logo B

I have selected 2 colours from the colour scheme (see below)-(as the colour of our logo is that).
However we would also like to see LIGHT CHOCOLATE BROWN or CHOCOLATE BROWN colour used as the background colour of the website
Preferred WEBSITE CONTENT:
1) HOME PAGE:
Content required=
--Company Logo
--Dr Rowan Pellfry
Paediatric Gastroenterologist & Hepatologist
-Lena Pellfry.
Dietitian & Nutritionist
--Website Menu (either listed horizontally or vertically):
Once clicked on each name:

Under each of the Website Menu items we want the following Headings to be added

2) ABOUT US page:
Sub-heading under this: Qualification, Skills, Special Interest

3) SERVICES
ROWAN'S PAGE: Individual Consultation, Endoscopy procedures
Individual Consultation, Group Based Services, Food Diary, Food & Symptom Diary

4) FEES & REBATE: Content as below:
Please Note: Payment of full fees is required at the time of consultation and procedures. 48 hours notice is required for cancellation of appointments/non-attendance. Failure to provide this may result in a fee being incurred. Please call reception to find out the amount of fee charged for cancellation of appointments/non-attendance.
headings are:
Paediatric Gastroenterology:
Rowan's pge
Individual Consultation - Initial (upto 30 mins):
Review Consultation (upto 15 mins):
Endoscopy procedures - No Gap fees charged. Fees will be billed directly to Vitacover. If any queries, please contact reception.

lena's pge
sub heading:
Individual Consultation - Initial (upto 45 mins):
Individual Consultation - Review (upto 30 mins):

Concession-Individual Consultation -Initial (upto 45 mins):
Concession-Individual Consultation - Review (upto 30 mins):
Please Note: Concession applies for health care card holders & pensioners

Group Based Services: Pricing subject to the type of service provided. Please contact us for an obligation free quote.
Education Topics Include:
- Paediatric Nutrition (Introducing Solids, Fussy Eating, Healthy Eating)
- Pregnancy Nutrition, Gestational Diabetes, Breastfeeding/Lactation Nutrition
- Healthy Eating, Supermarket Shopping Tips, Nutrition Label Reading Tips, Healthier
sub heading under nutrition & diet:
-Vitacover:
--A rebate of $52.95 is available from Vitacover if an EPC ( Enhanced Primary Care)/Chronic Disease Management (CDM) plan is issued by your GP.
--All mandatory paperwork needs to be available at the time of making your appointment for your eligibility.
-Private Health Fund:
--Most private health funds provide rebate on dietetic appointments. However the rebate amount depends on your level of cover. Thus, please contact your health fund to determine your entitled rebate.
-KRB: Approved provider for KRB services

6) FOR DOCTORS: Bright Meadow Paediatric Gastroenterologist Referral Form
Bright Meadow Dietitian Referral form
7) LOCATIONS & CONTACT

Paediatric Gastroenterology & Hepatology Service
Suite 46
Fairholt Grange Larchmont Medical Centre
17 Oswin Talbot Pde,
MURDOCH, WA 6150
P: (08) 9462 3051
F: (08) 9462 7309

Nutrition & Diet Service
Suite 46
17 Oswin Talbot Pde,
MURDOCH, WA 6150
P: (08) 9462 3051
F: (08) 9462 7309

Quill Medical Centre
52-54 Tarrago Parkway,
MANDURAH, WA 6210
P: (08) 9728 4402
F: (08) 96274518
www.qmcbaylow.com.au

This page should have a webform that has following titles:
-Your Name
-Your Email
-Your Phone
-Message

8) NEWS & BLOG
Nice to have
• We liked the design style of the websites below:
https://www.wellvorn.example/

http://tummyplex.example/

But feel free to use your creativity too
Should not have
• Please do not use any body building or muscle building images

```html
<!DOCTYPE html>
<html lang="en">
<head>
<meta charset="utf-8">
<title>Bright Meadow — Nutrition &amp; Gastrointestinal Health</title>
<link rel="stylesheet" href="https://fonts.googleapis.com/css2?family=Open+Sans:wght@300;400;700&family=Lora:ital,wght@1,400;1,700&display=swap">
<style>
  :root {
    --orange: #faa54b;
    --orange-soft: rgba(250, 165, 75, 0.88);
    --green: #acd036;
    --chocolate: #4a3e33;
    --chocolate-soft: rgba(66, 54, 44, 0.95);
    --paper: #f9f9f9;
    --nav-line: #dcdcdc;
    --nav-text: #4d4d4d;
    --white: #ffffff;
  }
  * { box-sizing: border-box; margin: 0; padding: 0; }
  html, body { width: 1200px; height: 925px; overflow: hidden; }
  body { position: relative; font-family: "Open Sans", Arial, sans-serif; background: var(--paper); }

  .hero-photo {
    position: absolute; left: 0; top: 0; width: 1200px; height: 846px;
    background:
      radial-gradient(ellipse at 80% 30%, #c98a78 0%, rgba(201,138,120,0) 40%),
      radial-gradient(ellipse at 25% 75%, #9a3a34 0%, rgba(154,58,52,0) 45%),
      radial-gradient(ellipse at 10% 90%, #c9d46a 0%, rgba(201,212,106,0) 35%),
      linear-gradient(180deg, #8fb56a 0%, #b8c98c 30%, #c7a486 55%, #a85a4a 80%, #b9b765 100%);
  }

  .brand-banner {
    position: absolute; left: 110px; top: 0; width: 202px; height: 365px;
    display: flex; align-items: center; justify-content: center; flex-direction: column; gap: 14px;
    padding-bottom: 70px;
  }
  .brand-banner svg { position: absolute; inset: 0; }
  .brand-mark { position: relative; width: 22px; height: 22px; border-radius: 50%; background: var(--orange); }
  .brand-name {
    position: relative; font-family: "Open Sans", sans-serif; font-weight: 700;
    font-size: 27px; line-height: 1.05; color: var(--orange); text-align: center; text-transform: uppercase;
  }

  .service-card { position: absolute; width: 287px; }
  .service-card .toggle {
    height: 39px; background: var(--orange-soft); color: var(--white);
    font-size: 24px; font-weight: 300; text-align: center; line-height: 38px;
  }
  .service-card .label {
    height: 53px; background: var(--chocolate-soft); color: var(--white);
    font-size: 13px; font-weight: 700; text-transform: uppercase;
    display: flex; align-items: center; justify-content: center; letter-spacing: 0.1px;
  }
  .service-card .details { background: var(--orange-soft); padding: 16px 18px 22px 19px; height: 245px; }
  .details h3 {
    font-family: "Lora", Georgia, serif; font-style: italic; font-weight: 700;
    font-size: 15px; color: var(--white); text-transform: uppercase;
    border-bottom: 2px solid var(--white); padding-bottom: 2px; margin-bottom: 12px;
  }
  .details p {
    font-family: "Lora", Georgia, serif; font-style: italic; font-size: 12.5px;
    line-height: 18px; color: var(--white); text-align: justify; margin-bottom: 30px;
  }
  .card-about { left: 111px; top: 671px; }
  .card-open { left: 457px; top: 427px; }
  .card-consult { left: 803px; top: 671px; }

  .site-nav {
    position: absolute; left: 0; top: 846px; width: 1200px; height: 79px;
    display: flex; background: var(--paper); border-top: 1px solid var(--nav-line);
  }
  .site-nav .cell {
    display: flex; align-items: center; justify-content: center; text-align: center;
    border-right: 1px solid var(--nav-line); font-size: 13px; color: var(--nav-text);
    text-transform: uppercase; line-height: 17px; letter-spacing: -0.2px;
  }
  .site-nav .home { width: 98px; background: var(--orange); border: 1px solid #e08d38; }
  .home-dot { width: 22px; height: 22px; border-radius: 50%; background: var(--white); }
  .site-nav .search { width: 64px; background: var(--orange); }
  .social { flex: 1; display: flex; align-items: center; padding-left: 16px; gap: 0; }
  .social span { width: 39px; height: 38px; border: 1px solid var(--nav-line); background: #f3f3f3; margin-left: -1px; }
  .social span.active { background: #3b579d; border-color: #3b579d; }
</style>
</head>
<body>
  <div class="hero-photo" role="img" aria-label="Mother and daughter smiling while choosing fresh apples at a supermarket produce stand"></div>

  <div class="brand-banner">
    <svg width="202" height="365" viewBox="0 0 202 365" aria-hidden="true">
      <polygon points="0,0 202,0 202,297 101,365 0,297" fill="#f9f9f9" fill-opacity="0.95"/>
    </svg>
    <div class="brand-mark"></div>
    <div class="brand-name">Bright<br>Meadow</div>
  </div>

  <div class="service-card card-about">
    <div class="toggle">+</div>
    <div class="label">About Bright Meadow</div>
  </div>

  <div class="service-card card-open">
    <div class="toggle">-</div>
    <div class="details">
      <h3>Nutrition and Diet</h3>
      <p>Lorem Ipsum is simply dummy text. Lorem Ipsum is simply dummy text. Lorem Ipsum is simply dummy text.</p>
      <h3>Gastrointestinal Health</h3>
      <p>Lorem Ipsum is simply dummy text. Lorem Ipsum is simply dummy text. Lorem Ipsum is simply dummy text.</p>
    </div>
    <div class="label">Consulting Services</div>
  </div>

  <div class="service-card card-consult">
    <div class="toggle">+</div>
    <div class="label">Consulting Services</div>
  </div>

  <nav class="site-nav">
    <div class="cell home"><div class="home-dot"></div></div>
    <div class="cell" style="width:183px">About Bright Meadow</div>
    <div class="cell" style="width:92px">Services</div>
    <div class="cell" style="width:97px">Product</div>
    <div class="cell" style="width:172px">Accredited Dietitian</div>
    <div class="cell" style="width:175px">Paediatric<br>Gastroenterologist</div>
    <div class="cell" style="width:98px">Contact</div>
    <div class="cell search">
      <svg width="11" height="11" viewBox="0 0 11 11" aria-label="Search"><circle cx="4.5" cy="4.5" r="3.3" fill="none" stroke="#fff" stroke-width="1.6"/><line x1="7" y1="7" x2="10" y2="10" stroke="#fff" stroke-width="1.8"/></svg>
    </div>
    <div class="social">
      <span class="active"></span><span></span><span></span><span></span><span></span>
    </div>
  </nav>
</body>
</html>
```